Tobias Wrenfield Business Card

In addition to my name design (file uploaded), black print on white card stock, e-mail address should be presented as a typical e-mail address, i.e., underlined and in blue ink, the card should include the following information:
Lecturer in Flight Operations Studies
Aviation Safety Review Consultant
Senior Certified Flight Instructor

twrenfield@qorvanet.net
Kenai, Alaska
(907) 518-2736

Industry/Entity Type

Business

```html
<!DOCTYPE html>
<html lang="en">
<head>
<meta charset="utf-8">
<title>Tobias Wrenfield Business Card</title>
<link rel="stylesheet" href="https://fonts.googleapis.com/css2?family=Oswald:wght@600&family=Open+Sans:wght@400&display=swap">
<style>
  :root {
    --bg: #e9e6e2;
    --card: #ffffff;
    --maroon: #3a1519;
    --grey: #5a5a5c;
    --ink: #111111;
    --light: #ffffff;
  }
  * { margin: 0; padding: 0; box-sizing: border-box; }
  html, body {
    width: 1200px;
    height: 900px;
    overflow: hidden;
    background: var(--bg);
  }
  .business-card {
    position: absolute;
    left: 100px;
    top: 165px;
    width: 1000px;
    height: 570px;
    background: var(--card);
    box-shadow: 0 10px 30px rgba(0,0,0,0.18);
    overflow: hidden;
  }
  .card-waves {
    position: absolute;
    inset: 0;
    width: 100%;
    height: 100%;
  }
  .card-name {
    position: absolute;
    left: 52px;
    top: 44px;
    font-family: "Oswald", sans-serif;
    font-weight: 600;
    font-size: 60px;
    line-height: 1.2;
    letter-spacing: 2px;
    color: var(--ink);
    text-transform: uppercase;
    white-space: nowrap;
  }
  .contact-block {
    position: absolute;
    right: 52px;
    top: 322px;
    list-style: none;
    text-align: right;
    font-family: "Open Sans", sans-serif;
    font-size: 25px;
    line-height: 36px;
    color: var(--light);
    white-space: nowrap;
  }
  .contact-line {
    display: flex;
    justify-content: flex-end;
    align-items: center;
    gap: 14px;
  }
  .contact-icon {
    width: 17px;
    height: 17px;
    fill: var(--light);
  }
  .contact-email {
    color: var(--light);
    text-decoration: none;
  }
</style>
</head>
<body>
  <div class="business-card">
    <svg class="card-waves" viewBox="0 0 1000 570" preserveAspectRatio="none" aria-hidden="true">
      <path class="wave-grey" fill="var(--grey)"
        d="M0,372 C180,395 360,360 560,300 C720,255 860,235 1000,232 L1000,250 C860,256 720,282 570,322 C380,380 190,420 0,412 Z"/>
      <path class="wave-maroon" fill="var(--maroon)"
        d="M0,430 C200,448 390,400 590,338 C750,290 880,268 1000,264 L1000,570 L0,570 Z"/>
      <path class="wave-line" fill="none" stroke="var(--light)" stroke-width="5"
        d="M0,470 C210,478 400,425 600,360 C760,310 880,290 1000,286"/>
    </svg>

    <h1 class="card-name">Tobias E. Wrenfield</h1>

    <ul class="contact-block">
      <li class="contact-line">
        <span>(907) 518-2736</span>
        <svg class="contact-icon" viewBox="0 0 24 24" aria-hidden="true"><path d="M6.6 10.8a15.1 15.1 0 0 0 6.6 6.6l2.2-2.2c.3-.3.7-.4 1-.2 1.1.4 2.3.6 3.6.6.6 0 1 .4 1 1V20c0 .6-.4 1-1 1C10.6 21 3 13.4 3 4c0-.6.4-1 1-1h3.5c.6 0 1 .4 1 1 0 1.3.2 2.5.6 3.6.1.3 0 .7-.2 1z"/></svg>
      </li>
      <li class="contact-line">
        <a class="contact-email" href="mailto:twrenfield@qorvanet.net">twrenfield@qorvanet.net</a>
        <svg class="contact-icon" viewBox="0 0 24 24" aria-hidden="true"><path d="M2 5h20v14H2z M4 7v.4l8 5.2 8-5.2V7z" fill-rule="evenodd"/></svg>
      </li>
      <li class="contact-line">Kenai, Alaska</li>
      <li class="contact-line">Lecturer in Flight Operations Studies</li>
      <li class="contact-line">Aviation Safety Review Consultant</li>
      <li class="contact-line">Senior Certified Flight Instructor</li>
    </ul>
  </div>
</body>
</html>
```